Flyer für Kampfsport und Selbstverteidigung
Zielgruppe
Kampfsportschule für Kinder/Jugendliche und Erwachsene
Martial Arts Wenk
Flyerbeispiel finden Sie im Anhang
Aufgabenstellung
Es soll modern gestaltet sein und mit den Farben: Schwarz, Grau, weiß und rot gearbeitet werden.
Im Anhang ist mein alter Flyer. Der soll als Beispiel für Inhalt und Stil sein.

```html
<!DOCTYPE html>
<html lang="de">
<head>
<meta charset="utf-8">
<title>Martial Arts Wenk – Flyer &amp; Trainingsplan</title>
<link href="https://fonts.googleapis.com/css2?family=Russo+One&family=Montserrat+Alternates:wght@500;600;700&display=swap" rel="stylesheet">
<style>
:root{
  --page:#e0e0e0;
  --red:#c8101c;
  --red-dark:#7a0a10;
  --black:#141414;
  --ink:#222;
  --grey:#9a9a9a;
  --light:#ececec;
  --white:#ffffff;
  --blue:#1f4d6e;
  --pink:#d0307a;
}
*{margin:0;padding:0;box-sizing:border-box}
html,body{width:1200px;height:2619px;overflow:hidden;background:var(--page)}
body{position:relative;font-family:"Montserrat Alternates",sans-serif;color:var(--white)}
.flyer{position:absolute;overflow:hidden;background:var(--black)}
.flyer--portrait{left:150px;top:99px;width:638px;height:905px}
.flyer--landscape{left:150px;top:1095px;width:905px;height:637px}
.flyer--plan{left:150px;top:1837px;width:903px;height:637px}
.bg{position:absolute;inset:0;width:100%;height:100%}
.brand{position:absolute;display:flex;flex-direction:column;align-items:center;justify-content:center;gap:10px}
.brand__dot{width:64px;height:64px;border-radius:50%;background:var(--red)}
.brand__name{font-family:"Russo One",sans-serif;color:var(--white);font-size:22px;white-space:nowrap}
.title{position:absolute;font-family:"Russo One",sans-serif;font-style:italic;text-align:center;white-space:nowrap;z-index:2;
  background:linear-gradient(#ffffff,#b9b9b9 55%,#f2f2f2);-webkit-background-clip:text;background-clip:text;color:transparent}
.subtitle{position:absolute;font-family:"Russo One",sans-serif;font-style:italic;text-align:center;line-height:1.05;color:var(--white);white-space:nowrap;z-index:2}
.band{position:absolute;background:linear-gradient(90deg,#fafafa 0%,#dcdcdc 60%,rgba(200,200,200,.6) 100%)}
.disc__head{position:absolute;font-family:"Russo One",sans-serif;color:var(--red);z-index:2}
.disc__item{position:absolute;font-weight:700;color:var(--ink);white-space:nowrap;z-index:2}
.disc__item::before{content:"• "}
.photo{position:absolute;z-index:1;background:radial-gradient(circle at 50% 22%,#f1c7a8 0 20%,transparent 21%),linear-gradient(170deg,rgba(255,120,140,.4),#1c1c1c 60%),var(--pink);border-radius:4px}
.photo--gi{background:linear-gradient(180deg,#f0d0b8 0 15%,#f4f4f4 15% 100%)}
.info-line{position:absolute;display:flex;align-items:center;gap:10px;font-size:19px;font-weight:500;white-space:nowrap}
.info-line::before,.info-line::after{content:"";flex:1;height:1px;background:var(--white)}
.contact{position:absolute;display:flex;gap:32px;font-size:21px;font-weight:600;white-space:nowrap}
.contact span{display:flex;align-items:center;gap:6px}
.contact svg{width:22px;height:22px}
.small{position:absolute;white-space:nowrap;font-weight:500}
.small b{font-family:"Russo One",sans-serif;font-weight:400}
.small .muted{color:var(--grey)}
.plan-table{position:absolute;left:183px;top:214px;width:679px;height:344px;border:4px solid var(--white);border-collapse:collapse;background:#f1f1f1;font-size:15px;text-align:center;line-height:1.15}
.plan-table th{background:var(--red);color:var(--white);font-weight:600;height:38px;font-size:15px}
.plan-table td{border-bottom:1px solid #bbb;color:var(--ink);font-weight:500}
.plan-table tr:last-child td{border-bottom:0}
.plan-table td.time{font-weight:600;color:var(--ink)}
.plan-table td.kb{color:var(--red)}
.plan-table td.u25{color:var(--blue)}
</style>
</head>
<body>

<section class="flyer flyer--portrait">
  <svg class="bg" viewBox="0 0 638 905" preserveAspectRatio="none">
    <rect width="638" height="449" fill="#1a1a1a"/>
    <polygon points="0,0 100,0 110,170 0,270" fill="#f2f2f2"/>
    <polygon points="638,0 560,0 540,160 638,270" fill="#f2f2f2"/>
    <polygon points="20,0 250,0 320,160 120,449 0,449 0,220" fill="#b00f18"/>
    <polygon points="618,0 390,0 320,160 520,449 638,449 638,220" fill="#9c0c14"/>
    <polygon points="100,120 320,0 540,120 520,449 120,449" fill="#2a2a2a" opacity=".85"/>
    <rect y="664" width="638" height="104" fill="#222"/>
    <polygon points="80,710 140,710 110,752" fill="#8f0c12"/>
    <polygon points="330,690 420,640 420,768 330,768" fill="#b00f18"/>
    <rect y="766" width="638" height="3" fill="var(--red)"/>
    <rect y="769" width="638" height="136" fill="#1b1b1b"/>
  </svg>
  <div class="brand" style="left:199px;top:29px;width:220px;height:177px">
    <div class="brand__dot"></div>
    <div class="brand__name">Martial Arts Wenk</div>
  </div>
  <div class="title" style="left:0;width:638px;top:212px;font-size:52px">MARTIAL ARTS</div>
  <div class="title" style="left:0;width:638px;top:268px;font-size:78px">WENK</div>
  <div class="subtitle" style="left:0;width:600px;top:364px;font-size:25px">KAMPFSPORT<br>&amp; SELBSTVERTEIDIGUNG</div>
  <div class="band" style="left:0;top:449px;width:638px;height:215px"></div>
  <div class="disc__head" style="left:30px;top:470px;font-size:35px">DISZIPLINEN:</div>
  <div class="disc__item" style="left:30px;top:513px;font-size:23px">Kick-Boxen/Sportkarate</div>
  <div class="disc__item" style="left:30px;top:548px;font-size:23px">Jiu-Jitsu Selbstverteidigung</div>
  <div class="disc__item" style="left:30px;top:583px;font-size:23px">Tricking</div>
  <div class="disc__item" style="left:30px;top:618px;font-size:23px">Ü25 Kick-Boxen</div>
  <div class="photo" role="img" aria-label="Foto: Mädchen im Kampfsport-Shirt mit pinken Boxhandschuhen und Gürtel" style="left:452px;top:438px;width:186px;height:330px"></div>
  <div class="small" style="left:0;width:638px;text-align:center;top:778px;font-size:20px"><span class="muted">Leitung: </span><b>Jonas Wenk</b></div>
  <div class="small" style="left:0;width:638px;text-align:center;top:806px;font-size:16px">Am Werkhof 7b &nbsp;|&nbsp; 26340 Zetel</div>
  <div class="info-line" style="left:28px;width:582px;top:834px">INFO &amp; PROBETRAINING:</div>
  <div class="contact" style="left:28px;top:860px">
    <span><svg viewBox="0 0 24 24"><circle cx="12" cy="12" r="10" fill="none" stroke="var(--red)" stroke-width="2"/><path d="M8 7l2 0 1 3-1.5 1a6 6 0 0 0 3.5 3.5l1-1.5 3 1v2a2 2 0 0 1-2 1A9 9 0 0 1 7 9a2 2 0 0 1 1-2z" fill="var(--red)"/></svg>0151 / 2203 9184</span>
    <span><svg viewBox="0 0 24 24"><rect x="2" y="5" width="20" height="14" fill="none" stroke="var(--red)" stroke-width="2"/><path d="M2 5l10 8 10-8" fill="none" stroke="var(--red)" stroke-width="2"/></svg>info@martial-arts-wenk.de</span>
  </div>
</section>

<section class="flyer flyer--landscape">
  <svg class="bg" viewBox="0 0 905 637" preserveAspectRatio="none">
    <rect width="905" height="317" fill="#1d1d1d"/>
    <polygon points="0,0 60,0 0,90" fill="#f0f0f0"/>
    <polygon points="20,0 90,0 0,150 0,40" fill="#b00f18"/>
    <polygon points="0,160 150,60 220,317 0,317" fill="#a50e16"/>
    <polygon points="905,0 840,0 780,110 905,60" fill="#c8101c"/>
    <polygon points="905,80 860,150 905,230" fill="#f0f0f0"/>
    <polygon points="880,180 905,150 905,317 850,317" fill="#9c0c14"/>
    <rect y="454" width="905" height="183" fill="#1f1f1f"/>
    <polygon points="330,454 460,454 380,520" fill="#2c2c2c"/>
  </svg>
  <div class="brand" style="left:40px;top:58px;width:260px;height:214px">
    <div class="brand__dot" style="width:78px;height:78px"></div>
    <div class="brand__name" style="font-size:25px">Martial Arts Wenk</div>
  </div>
  <div class="title" style="left:300px;width:506px;top:58px;font-size:55px">MARTIAL ARTS</div>
  <div class="title" style="left:300px;width:506px;top:118px;font-size:78px">WENK</div>
  <div class="subtitle" style="left:300px;width:480px;top:210px;font-size:26px">KAMPFSPORT<br>&amp; SELBSTVERTEIDIGUNG</div>
  <div class="band" style="left:0;top:317px;width:905px;height:137px"></div>
  <div class="disc__head" style="left:60px;top:343px;font-size:31px">DISZIPLINEN:</div>
  <div class="disc__item" style="left:60px;top:381px;font-size:22px">Kick-Boxen/Sportkarate</div>
  <div class="disc__item" style="left:60px;top:411px;font-size:22px">Jiu-Jitsu Selbstverteidigung</div>
  <div class="disc__item" style="left:422px;top:381px;font-size:22px">Tricking</div>
  <div class="disc__item" style="left:422px;top:411px;font-size:22px">Ü25 Kick-Boxen</div>
  <div class="photo" role="img" aria-label="Foto: Mädchen im Kampfsport-Shirt mit pinken Boxhandschuhen und Gürtel" style="left:660px;top:292px;width:245px;height:345px"></div>
  <div class="info-line" style="left:45px;width:585px;top:524px">INFO &amp; PROBETRAINING:</div>
  <div class="contact" style="left:45px;top:551px">
    <span><svg viewBox="0 0 24 24"><circle cx="12" cy="12" r="10" fill="none" stroke="var(--red)" stroke-width="2"/><path d="M8 7l2 0 1 3-1.5 1a6 6 0 0 0 3.5 3.5l1-1.5 3 1v2a2 2 0 0 1-2 1A9 9 0 0 1 7 9a2 2 0 0 1 1-2z" fill="var(--red)"/></svg>0151 / 2203 9184</span>
    <span><svg viewBox="0 0 24 24"><rect x="2" y="5" width="20" height="14" fill="none" stroke="var(--red)" stroke-width="2"/><path d="M2 5l10 8 10-8" fill="none" stroke="var(--red)" stroke-width="2"/></svg>info@martial-arts-wenk.de</span>
  </div>
  <div class="small" style="left:43px;top:596px;font-size:17px"><span class="muted" style="font-size:20px">Leitung: </span><b style="font-size:20px">Jonas Wenk</b>&nbsp; Am Werkhof 7b &nbsp;|&nbsp; 26340 Zetel</div>
</section>

<section class="flyer flyer--plan">
  <svg class="bg" viewBox="0 0 903 637" preserveAspectRatio="none">
    <rect width="903" height="637" fill="#161616"/>
    <polygon points="0,0 240,0 100,120 0,60" fill="#b00f18"/>
    <polygon points="0,20 60,0 0,120" fill="#f0f0f0"/>
    <polygon points="560,0 903,0 903,120 700,200 560,60" fill="#a50e16"/>
    <polygon points="903,0 903,40 860,0" fill="#f0f0f0"/>
    <polygon points="250,190 903,190 903,637 250,637" fill="#8a0b12"/>
    <polygon points="820,637 903,560 903,637" fill="#d9d9d9"/>
  </svg>
  <div class="brand" style="left:100px;top:37px;width:183px;height:152px">
    <div class="brand__dot" style="width:54px;height:54px"></div>
    <div class="brand__name" style="font-size:18px">Martial Arts Wenk</div>
  </div>
  <div class="title" style="left:285px;width:600px;top:72px;font-size:60px">TRAININGSPLAN</div>
  <div class="title" style="left:285px;width:580px;top:136px;font-size:46px">MARTIAL ARTS WENK</div>
  <div class="photo photo--gi" role="img" aria-label="Foto: Mädchen im weißen Karateanzug mit gelbem Gürtel in Kampfhaltung" style="left:24px;top:176px;width:153px;height:442px"></div>
  <table class="plan-table">
    <tr><th>ZEIT</th><th>MONTAG</th><th>DIENSTAG</th><th>MITTWOCH</th><th>DONNERSTAG</th><th>FREITAG</th></tr>
    <tr><td class="time">15:00<br>15:50</td><td class="kb">Kick-Boxen<br>3-5 Jahre</td><td>Jiu-Jitsu<br>3-6 Jahre</td><td class="kb">Kick-Boxen<br>3-5 Jahre</td><td>Jiu-Jitsu<br>3-6 Jahre</td><td class="kb">Kick-Boxen<br>3-6 Jahre</td></tr>
    <tr><td class="time">16:00<br>16:50</td><td class="kb">Kick-Boxen<br>6-7 Jahre</td><td>Jiu-Jitsu<br>7-12 Jahre</td><td class="kb">Kick-Boxen<br>6-7 Jahre</td><td>Jiu-Jitsu<br>7-12 Jahre</td><td class="kb" style="font-size:12px;line-height:1">Kick-Boxen<br>ab 7 Jahre<br>Ab Gelbgurt</td></tr>
    <tr><td class="time">17:00<br>18:00</td><td class="kb">Kick-Boxen<br>8-10 Jahre</td><td class="kb">Tricking<br>ab 6 Jahre</td><td class="kb">Kick-Boxen<br>8-10 Jahre</td><td class="kb">Tricking<br>ab 6 Jahre</td><td></td></tr>
    <tr><td class="time">18:15<br>19:15</td><td class="kb">Kick-Boxen<br>10-12 Jahre</td><td class="u25">Kick-Boxen<br>Ü25 Gruppe</td><td class="kb">Kick-Boxen<br>10-12 Jahre</td><td class="u25">Kick-Boxen<br>Ü25 Gruppe</td><td></td></tr>
    <tr><td class="time">19:30<br>21:00</td><td class="kb">Kick-Boxen<br>ab 13 Jahre</td><td></td><td class="kb">Kick-Boxen<br>ab 13 Jahre</td><td></td><td></td></tr>
  </table>
  <div class="small" style="left:181px;top:565px;font-size:21px">Info &amp; Probetraining:</div>
  <div class="contact" style="left:181px;top:594px">
    <span><svg viewBox="0 0 24 24"><circle cx="12" cy="12" r="10" fill="none" stroke="var(--red)" stroke-width="2"/><path d="M8 7l2 0 1 3-1.5 1a6 6 0 0 0 3.5 3.5l1-1.5 3 1v2a2 2 0 0 1-2 1A9 9 0 0 1 7 9a2 2 0 0 1 1-2z" fill="var(--red)"/></svg>0151 / 2203 9184</span>
    <span><svg viewBox="0 0 24 24"><rect x="2" y="5" width="20" height="14" fill="none" stroke="var(--red)" stroke-width="2"/><path d="M2 5l10 8 10-8" fill="none" stroke="var(--red)" stroke-width="2"/></svg>info@martial-arts-wenk.de</span>
  </div>
</section>

</body>
</html>
```